Bold Website Redesign for a Disruptive Training Brand

Brightmoor Labs is a bold, no-fluff sales & leadership training company powered by AI-driven practice and behavioral science. We’ve already built our website structure and copy in Craftly.io — now we need a designer to fully transform the visual design across all pages (Home, Approach, Programs, About, Contact).
We’re looking for a modern, memorable, high-performance aesthetic that blends human energy, science, and tech without feeling corporate or safe. Clean, bold typography, fluid layout, strong emotional hero moments, subtle motion, and imagery that mixes real people with abstract scientific/tech visuals.Because our clients are primarily North American, please ensure any human photography or AI-generated imagery reflects a North American business context and demographics (modern, diverse, and realistic).

Your job is visual redesign only — no coding required.
The final design must be practical to rebuild inside Craftly.io.

A full, detailed creative brief (plus logo files) is included in the uploaded files.
If you can bring a mix of edge, intelligence, and strong visual storytelling, we’d love to see your work.

Website is already built in Craftly.io at - https://brightmoor-website-tempdesign.craftly.app — structure is set, visuals need redesign.

```html
<!DOCTYPE html>
<html lang="en">
<head>
<meta charset="utf-8">
<title>Brightmoor Labs — Training That Practices Back</title>
<link href="https://fonts.googleapis.com/css2?family=Playfair+Display:wght@700;800&family=Nunito+Sans:wght@400;600&family=Inter:wght@500&display=swap" rel="stylesheet">
<style>
:root{
  --ink:#111418;
  --white:#ffffff;
  --hero-a:#4a72c2;
  --hero-b:#45c5ec;
  --cyan:#13c0ef;
  --navy:#04365c;
  --soft:#eef8fd;
  --lavender:#dbe5fb;
  --chart:#46bde6;
  --muted:#2b3440;
}
*{margin:0;padding:0;box-sizing:border-box}
html,body{width:1200px;height:2699px;overflow:hidden}
body{position:relative;background:var(--white);font-family:"Nunito Sans",sans-serif;color:var(--ink)}
.serif{font-family:"Playfair Display",serif;font-weight:700}
.abs{position:absolute}
.btn{position:absolute;display:flex;align-items:center;justify-content:center;border-radius:24px;font-family:"Inter",sans-serif;font-weight:500;font-size:13px}
.btn-light{background:var(--white);color:var(--ink)}
.btn-cyan{background:var(--cyan);color:var(--white)}

/* hero */
.hero{position:absolute;left:0;top:0;width:1200px;height:563px;background:linear-gradient(100deg,var(--hero-a) 0%,#4b93d6 50%,var(--hero-b) 100%);overflow:hidden}
.hero-visual{position:absolute;left:640px;top:90px;width:560px;height:473px;background:radial-gradient(ellipse at 55% 45%,rgba(255,255,255,.32) 0%,rgba(255,255,255,.12) 45%,rgba(255,255,255,0) 70%)}
.nav{position:absolute;left:172px;top:25px;width:855px;height:59px;background:var(--white);border-radius:30px}
.brand{position:absolute;display:flex;align-items:center;gap:10px;font-family:"Nunito Sans",sans-serif;font-weight:600;letter-spacing:.3px}
.brand-dot{width:30px;height:30px;border-radius:50%}
.nav .brand{left:24px;top:14px;font-size:20px;color:#1b2433}
.nav .brand-dot{background:#4a72c2}
.nav-links{position:absolute;left:412px;top:22px;display:flex;gap:29px;font-family:"Inter",sans-serif;font-size:12px;color:#222}
.nav .btn{left:762px;top:5px;width:87px;height:49px;font-size:12px;border-radius:25px}
.hero h1{position:absolute;left:172px;top:153px;font-size:69px;line-height:69px;color:var(--white)}
.hero .lead{position:absolute;left:172px;top:303px;width:380px;font-size:19px;line-height:26px;color:var(--white)}
.hero .body{position:absolute;left:172px;top:369px;width:420px;font-size:12.5px;line-height:18px;color:var(--white)}
.hero .btn{left:172px;top:424px;width:142px;height:44px}

/* problem */
.chart-card{position:absolute;left:172px;top:627px;width:419px;height:308px;background:var(--soft);border-radius:14px}
.chart-card .caption{position:absolute;left:0;width:100%;top:271px;text-align:center;font-size:12.5px;color:#1b2433}
.problem h2{position:absolute;left:628px;top:663px;width:420px;font-size:40px;line-height:48px}
.problem p{position:absolute;left:628px;top:828px;width:400px;font-size:12.5px;line-height:18px;color:var(--muted)}

/* practice */
.practice-bg{position:absolute;left:0;top:960px;width:1200px;height:476px;background:linear-gradient(180deg,#ffffff 0%,var(--lavender) 100%)}
.practice h2{position:absolute;left:0;width:1200px;top:1012px;text-align:center;font-size:40px;line-height:48px}
.practice .sub{position:absolute;left:0;width:1200px;top:1059px;text-align:center;font-size:12.5px;color:var(--muted)}
.card{position:absolute;top:1114px;width:273px;height:247px;background:var(--white);border-radius:12px;text-align:center}
.card .icon{position:absolute;left:100px;top:32px;width:74px;height:74px;border-radius:50%;background:#eef3fd}
.card .icon svg{position:absolute;left:22px;top:22px}
.card h3{position:absolute;left:0;width:100%;top:120px;font-size:23px}
.card p{position:absolute;left:30px;width:213px;top:157px;font-size:11px;line-height:16.5px;color:var(--muted)}

/* team */
.team-bg{position:absolute;left:0;top:1436px;width:1200px;height:560px;background:radial-gradient(ellipse at 50% 45%,#d5eef9 0%,#f2f9fd 60%,#ffffff 100%)}
.team h2{position:absolute;left:172px;top:1550px;width:420px;font-size:40px;line-height:48px}
.team p{position:absolute;left:172px;top:1712px;width:400px;font-size:12.5px;line-height:18px;color:var(--muted)}
.team .btn{left:172px;top:1807px;width:137px;height:44px}
.team-photo{position:absolute;left:631px;top:1509px;width:398px;height:398px;border-radius:50%;background:linear-gradient(160deg,#c8def5 0%,#6e8fbf 55%,#2b3550 100%)}

/* cta */
.footer-bg{position:absolute;left:0;top:2233px;width:1200px;height:466px;background:var(--navy)}
.cta{position:absolute;left:172px;top:1988px;width:855px;height:331px;border-radius:24px;background:linear-gradient(100deg,#4a72c2 0%,#4a9bd9 55%,#44c5ec 100%);overflow:hidden}
.cta-visual{position:absolute;left:30px;top:20px;width:390px;height:311px;background:radial-gradient(ellipse at 50% 50%,rgba(255,255,255,.28) 0%,rgba(255,255,255,.08) 55%,rgba(255,255,255,0) 75%)}
.cta h2{position:absolute;left:457px;top:64px;width:360px;font-size:40px;line-height:48px;color:var(--white)}
.cta .btn{left:457px;top:227px;width:159px;height:44px}

/* footer */
.footer .brand{left:176px;top:2400px;font-size:20px;color:var(--white)}
.footer .brand-dot{background:#4d9fe0}
.footer .tagline{position:absolute;left:172px;top:2447px;width:270px;font-size:12.5px;line-height:18px;color:#dfe8f2}
.social{position:absolute;top:2508px;width:26px;height:26px;border:2px solid var(--white);border-radius:50%}
.fcol{position:absolute;top:2400px}
.fcol h4{font-family:"Playfair Display",serif;font-weight:700;font-size:15px;color:var(--white);margin-bottom:20px}
.fcol a{display:block;font-size:11.5px;color:#dfe8f2;text-decoration:none;line-height:14px;margin-bottom:16px}
.contact-row{display:flex;gap:10px;font-size:11.5px;line-height:14px;color:#dfe8f2;margin-bottom:16px}
.divider{position:absolute;left:0;top:2621px;width:1200px;height:1px;background:rgba(255,255,255,.12)}
.copy{position:absolute;left:0;width:1200px;top:2652px;text-align:center;font-size:11.5px;color:#dfe8f2}
</style>
</head>
<body>

<section class="hero">
  <div class="hero-visual" role="img" aria-label="Abstract particle-dot profile of a human head in white on blue"></div>
  <nav class="nav">
    <div class="brand"><span class="brand-dot"></span>BRIGHTMOOR LABS</div>
    <div class="nav-links"><span>Home</span><span>Approach</span><span>Programs</span><span>About</span><span>Contact</span></div>
    <div class="btn btn-cyan">Let's Talk</div>
  </nav>
  <h1 class="serif">Training That<br>Practices Back.</h1>
  <p class="lead">AI-Driven Sustainment That Builds Mastery — So You Don't Have To.</p>
  <p class="body">You'll See Measurable Growth As Your People Turn Insight Into Habit — Automatically, Sustainably, And Without Extra Work For Their Leaders.</p>
  <div class="btn btn-light">See How We Do It</div>
</section>

<section class="problem">
  <div class="chart-card">
    <svg width="419" height="280" viewBox="0 0 400 267">
      <defs>
        <linearGradient id="fade" x1="0" y1="0" x2="0" y2="1">
          <stop offset="0" stop-color="#46bde6" stop-opacity=".75"/>
          <stop offset="1" stop-color="#46bde6" stop-opacity="0"/>
        </linearGradient>
      </defs>
      <path d="M28 32 L108 58 L172 135 L222 140 L259 162 L307 149 L380 206 L380 240 L28 240 Z" fill="url(#fade)"/>
      <g stroke="#ffffff" stroke-opacity=".6" stroke-width="1">
        <line x1="108" y1="58" x2="108" y2="240"/><line x1="172" y1="135" x2="172" y2="240"/>
        <line x1="222" y1="140" x2="222" y2="240"/><line x1="259" y1="162" x2="259" y2="240"/>
        <line x1="307" y1="149" x2="307" y2="240"/>
      </g>
      <polyline points="28,32 108,58 172,135 222,140 259,162 307,149 380,206" fill="none" stroke="#46bde6" stroke-width="1.4"/>
      <g fill="#46bde6">
        <circle cx="28" cy="32" r="3"/><circle cx="108" cy="58" r="3"/><circle cx="172" cy="135" r="3"/>
        <circle cx="222" cy="140" r="3"/><circle cx="259" cy="162" r="3"/><circle cx="307" cy="149" r="3"/><circle cx="380" cy="206" r="3"/>
      </g>
      <g font-family="Nunito Sans, sans-serif" font-size="8.5" fill="#1b2433">
        <text x="74" y="39">People Forget Fast</text>
        <text x="169" y="96">Within A Week, 70% Is Gone</text>
        <text x="311" y="138">We Built The Fix In.</text>
      </g>
    </svg>
    <div class="caption">Watch How Sustained Practice Changes The Curve &nbsp;<span style="color:#46bde6">↗</span></div>
  </div>
  <h2 class="serif">The Real Problem Isn't Your People — It's The Forgetting Curve.</h2>
  <p>Within A Week, Most Training Disappears. Leaders Are Left Guessing Who's Using What They Learned — And No One Has Time To Fix It. We Built Brightmoor Labs To Make Progress Automatic, Measurable, And Real.</p>
</section>

<section class="practice">
  <div class="practice-bg"></div>
  <h2 class="serif">Practice Made Permanent</h2>
  <p class="sub">You'll Replace "Hope They Remember" With A System That Makes Sure They Do.</p>
  <div class="card" style="left:172px">
    <div class="icon"><svg width="30" height="30" viewBox="0 0 30 30" fill="none" stroke="#3f8fd8" stroke-width="1.6"><rect x="4" y="5" width="22" height="15" rx="2"/><path d="M15 8v10M8 9c3 0 5 1 7 3M22 9c-3 0-5 1-7 3M12 25h6M15 20v5"/></svg></div>
    <h3 class="serif">Learn</h3>
    <p>Fast, Focused Workshops, Built On Science, That Install The Mindset And Skills That Matter Most.</p>
  </div>
  <div class="card" style="left:463px">
    <div class="icon"><svg width="30" height="30" viewBox="0 0 30 30" fill="none" stroke="#3f8fd8" stroke-width="1.6"><circle cx="15" cy="15" r="12"/><circle cx="15" cy="15" r="8"/><path d="M11 15l3 3 5-6"/></svg></div>
    <h3 class="serif">Certify</h3>
    <p>Programmatic AI-Driven Practice And Feedback - Mastery Without Management Overhead.</p>
  </div>
  <div class="card" style="left:754px">
    <div class="icon"><svg width="30" height="30" viewBox="0 0 30 30" fill="none" stroke="#3f8fd8" stroke-width="1.6"><circle cx="15" cy="17" r="8"/><circle cx="15" cy="17" r="3"/><path d="M15 9V3M11 6l4 3 4-3"/></svg></div>
    <h3 class="serif">Sustain</h3>
    <p>Light-Touch Challenges And Dashboards That Keep Skills Sharp Long After Training Ends.</p>
  </div>
</section>

<section class="team">
  <div class="team-bg"></div>
  <h2 class="serif">Built By People Who've Led The Change Themselves.</h2>
  <p>Behind Brightmoor Labs Are Leaders Who've Lived The Challenge Of Making Learning Last. They've Scaled Companies, Built Cultures, And Led Transformation — And Now They've Designed The System They Always Wished Existed.</p>
  <div class="btn btn-cyan">Meet the Team</div>
  <div class="team-photo" role="img" aria-label="Photo of two business professionals in suits smiling while looking at a tablet"></div>
</section>

<footer class="footer">
  <div class="footer-bg"></div>
  <div class="cta">
    <div class="cta-visual" role="img" aria-label="Wireframe illustration of a robot figure holding a glowing brain"></div>
    <h2 class="serif">Ready To See What Lasting Capability Looks Like?</h2>
    <div class="btn btn-light">Start A Conversation</div>
  </div>
  <div class="brand"><span class="brand-dot"></span>BRIGHTMOOR LABS</div>
  <p class="tagline">Making Learning That Sticks Through AI-Driven Sustainment And Behavioral Science.</p>
  <span class="social" style="left:172px" aria-label="Social profile"></span>
  <span class="social" style="left:220px" aria-label="Social profile"></span>
  <div class="fcol" style="left:524px"><h4>Certify</h4><a>Home</a><a>Approach</a><a>Programs</a><a>About</a><a>Contact</a></div>
  <div class="fcol" style="left:650px"><h4>Legal</h4><a>Privacy Policy</a><a>Terms And Conditions</a></div>
  <div class="fcol" style="left:841px"><h4>Contact</h4>
    <div class="contact-row"><svg width="16" height="14" viewBox="0 0 16 14" fill="none" stroke="#fff" stroke-width="1.2"><rect x="1" y="1.5" width="14" height="11" rx="2"/><path d="M2 3l6 5 6-5"/></svg>Contact@Brightmoorlabs.Com</div>
    <div class="contact-row"><svg width="16" height="16" viewBox="0 0 16 16" fill="none" stroke="#fff" stroke-width="1.2"><path d="M3 1.5l3 .5 1 3-2 1.5c1 2 2.5 3.5 4.5 4.5L11 9l3 1 .5 3c-.5 1-1.5 1.5-2.5 1.5C6 14 2 10 1.5 4c0-1 .5-2 1.5-2.5z"/></svg>+1 (555) 014-2200</div>
    <div class="contact-row"><svg width="16" height="16" viewBox="0 0 16 16" fill="none" stroke="#fff" stroke-width="1.2"><circle cx="8" cy="8" r="6.5"/><circle cx="8" cy="7" r="2"/></svg><span>4820 Harbor Ridge Rd Suite 210<br>Mesa, AZ 85201</span></div>
  </div>
  <div class="divider"></div>
  <p class="copy">© 2024 Brightmoor Labs. All rights reserved.</p>
</footer>

</body>
</html>
```